Bref créative
Turnip Cuddler LLC
Embracing More Plant-Based Eating for Everyone
Bright & Fun-filled
Paula J. Mercer
Health & Wellness Coach, NQRS Certified
418 Marlow Ln.
Georgetown, KY 40871
theturnipcuddler@mailnest.example
www.turnipcuddler.example
http://twitter.com/TurnipCuddler
I do not want to have the address on the card.
Just the logo?

```html
<!DOCTYPE html>
<html lang="en">
<head>
<meta charset="utf-8">
<title>Turnip Cuddler – Business Card</title>
<link href="https://fonts.googleapis.com/css2?family=Questrial&display=swap" rel="stylesheet">
<style>
  :root {
    --backdrop: #ecebe8;
    --card: #ffffff;
    --card-edge: #f1f1f1;
    --leaf-green: #5a9a2c;
    --bark-brown: #7a5b40;
    --ink: #555555;
    --muted: #777777;
    --shadow: rgba(0, 0, 0, 0.18);
  }
  html, body {
    margin: 0;
    padding: 0;
    overflow: hidden;
  }
  body {
    width: 1200px;
    height: 972px;
    background: var(--backdrop);
    position: relative;
    font-family: "Questrial", "Century Gothic", sans-serif;
  }
  .card {
    position: absolute;
    width: 560px;
    height: 318px;
    background: linear-gradient(135deg, var(--card) 0%, var(--card-edge) 100%);
    border-radius: 16px;
    box-shadow: 0 10px 28px var(--shadow);
    overflow: hidden;
  }
  .card--front { left: 150px; top: 130px; }
  .card--back  { left: 490px; top: 520px; }

  .brand {
    display: flex;
    align-items: center;
    gap: 10px;
  }
  .brand__dot {
    border-radius: 50%;
    background: var(--bark-brown);
    flex: none;
  }
  .brand__name {
    color: var(--leaf-green);
    white-space: nowrap;
  }

  .card--front .brand {
    position: absolute;
    left: 44px;
    top: 62px;
  }
  .card--front .brand__name { font-size: 46px; }
  .card--front .brand__dot { width: 22px; height: 22px; }

  .contact {
    position: absolute;
    left: 46px;
    top: 172px;
    color: var(--ink);
    font-size: 12.5px;
    line-height: 1.4;
  }
  .contact__name {
    color: var(--leaf-green);
    font-size: 15px;
    margin: 0;
  }
  .contact__title {
    margin: 0 0 14px;
  }
  .contact__line { margin: 0; }
  .contact__social {
    display: flex;
    align-items: center;
    gap: 6px;
  }
  .contact__social-mark {
    width: 11px;
    height: 11px;
    border-radius: 2px;
    background: var(--muted);
  }
  .contact__web {
    margin: 14px 0 0;
    color: var(--leaf-green);
  }

  .card--back .brand {
    position: absolute;
    right: 34px;
    bottom: 30px;
    flex-direction: column;
    align-items: flex-end;
    gap: 6px;
  }
  .card--back .brand__row {
    display: flex;
    align-items: center;
    gap: 8px;
  }
  .card--back .brand__name { font-size: 22px; }
  .card--back .brand__dot { width: 12px; height: 12px; }
  .card--back .brand__web {
    color: var(--leaf-green);
    font-size: 12.5px;
  }
</style>
</head>
<body>
  <section class="card card--front" aria-label="Card front">
    <div class="brand">
      <span class="brand__name">Turnip Cuddler</span>
      <span class="brand__dot" aria-hidden="true"></span>
    </div>
    <div class="contact">
      <p class="contact__name">Paula J. Mercer</p>
      <p class="contact__title">Health &amp; Wellness Coach, NQRS Certified</p>
      <p class="contact__line">Phone: 859-555-0142</p>
      <p class="contact__line">Email: theturnipcuddler@mailnest.example</p>
      <p class="contact__line contact__social"><span class="contact__social-mark" aria-hidden="true"></span>TurnipCuddler</p>
      <p class="contact__web">www.turnipcuddler.example</p>
    </div>
  </section>

  <section class="card card--back" aria-label="Card back">
    <div class="brand">
      <div class="brand__row">
        <span class="brand__name">Turnip Cuddler</span>
        <span class="brand__dot" aria-hidden="true"></span>
      </div>
      <span class="brand__web">www.turnipcuddler.example</span>
    </div>
  </section>
</body>
</html>
```